Design a Mobile App for Landscape Businesses

This project is to design the first three screens for a mobile app for Landscape and Lawncare businesses. This app will serve as a directory for homeowners to locate landscape and lawn care businesses and for landscape businesses and contractors to run their business. See the attached PDF for more information and example
Here is the link to the description https://brevlinq.test/k3r92P

Target Market(s)

Landscape and lawn care business, gardeners, home owners

Industry/Entity Type

Landscape Gardening

Logo Text

Quillmoray

Colors

Designer to choose colors to be used in the design.

```html
<!DOCTYPE html>
<html lang="en">
<head>
<meta charset="utf-8">
<title>Quillmoray – Business Listing</title>
<link href="https://fonts.googleapis.com/css2?family=Montserrat:wght@400;500;600&display=swap" rel="stylesheet">
<style>
  :root {
    --green: #2bbf86;
    --green-dark: #22a874;
    --page: #eeeeee;
    --screen-bg: #ebebeb;
    --card: #ffffff;
    --ink: #222222;
    --body-text: #555555;
    --star: #f5c518;
    --media-tone: #e2e6df;
    --photo-tone-a: #7fae5a;
    --photo-tone-b: #5f9a3a;
  }
  * { box-sizing: border-box; margin: 0; padding: 0; }
  html, body {
    width: 1200px; height: 1200px; overflow: hidden;
    background: var(--page);
    font-family: "Montserrat", sans-serif;
  }
  .screen {
    position: absolute; left: 343px; top: 0;
    width: 514px; height: 1200px;
    background: var(--screen-bg);
    overflow: hidden;
  }
  .app-header {
    position: absolute; left: 0; top: 0; width: 514px; height: 106px;
    background: var(--green);
  }
  .brand {
    position: absolute; left: 12px; top: 43px;
    color: #fff; font-weight: 600; font-size: 13px; letter-spacing: 0.2px;
  }
  .search {
    position: absolute; left: 99px; top: 30px; width: 286px; height: 46px;
    background: #fff; border-radius: 23px;
  }
  .search-text {
    position: absolute; left: 15px; top: 14px; font-size: 14px; color: #444;
  }
  .search-btn { position: absolute; right: 4px; top: 6px; }
  .login {
    position: absolute; left: 397px; top: 40px; display: flex; align-items: center; gap: 8px;
    color: #fff; font-weight: 600; font-size: 14px;
  }
  .card {
    position: absolute; left: 16px; top: 124px; width: 481px; height: 1059px;
    background: var(--card);
  }
  .biz-name {
    position: absolute; left: 16px; top: 12px;
    color: var(--green); font-size: 19px; font-weight: 500;
  }
  .biz-sub {
    position: absolute; left: 16px; top: 38px;
    color: var(--green); font-size: 10px;
  }
  .biz-mark {
    position: absolute; left: 424px; top: 15px; width: 32px; height: 32px;
    border-radius: 50%; background: var(--green);
  }
  .card-rule {
    position: absolute; left: 0; top: 61px; width: 481px; height: 3px; background: var(--green);
  }
  .media {
    position: absolute; left: 0; top: 64px; width: 481px; height: 212px;
    background: var(--media-tone);
  }
  .media-label {
    position: absolute; left: 16px; top: 140px; font-size: 12px; color: #777;
  }
  .about-title {
    position: absolute; left: 25px; top: 297px;
    color: var(--green); font-size: 17px; font-weight: 500;
  }
  .about-text {
    position: absolute; left: 25px; top: 330px; width: 425px;
    font-size: 10.9px; line-height: 13.7px; letter-spacing: -0.15px;
    color: var(--body-text); text-align: justify;
  }
  .services {
    position: absolute; left: 26px; top: 481px; width: 430px;
    display: grid; grid-template-columns: 211px 211px; row-gap: 6px;
    list-style: none;
  }
  .services li {
    font-size: 11.5px; font-weight: 600; color: var(--ink);
    display: flex; align-items: center; gap: 7px; height: 14.5px;
  }
  .services li::before {
    content: ""; width: 9px; height: 9px; background: var(--green); flex: none;
  }
  .gallery-title {
    position: absolute; left: 28px; top: 570px;
    color: var(--green); font-size: 17px; font-weight: 500;
  }
  .photo {
    position: absolute; top: 615px; width: 200px; height: 165px;
    background: linear-gradient(180deg, var(--photo-tone-a), var(--photo-tone-b));
  }
  .photo-house { left: 27px; }
  .photo-garden { left: 252px; }
  .contact {
    position: absolute; display: flex; align-items: center; gap: 8px;
    font-size: 11px; color: var(--green);
  }
  .contact svg { flex: none; }
  .rating {
    position: absolute; left: 0; top: 943px; width: 481px;
    display: flex; justify-content: center; align-items: center; gap: 6px;
    font-size: 13.5px; color: var(--ink);
  }
  .stars { display: flex; gap: 4px; }
  .quote-btn {
    position: absolute; left: 29px; top: 983px; width: 420px; height: 45px;
    border: 1.5px solid var(--green); border-radius: 23px;
    display: flex; align-items: center; justify-content: center;
    color: var(--green-dark); font-size: 17px; font-weight: 600;
  }
</style>
</head>
<body>
<div class="screen">
  <header class="app-header">
    <div class="brand">Quillmoray</div>
    <div class="search">
      <span class="search-text">Lawn Care</span>
      <svg class="search-btn" width="34" height="34" viewBox="0 0 34 34" aria-hidden="true">
        <circle cx="17" cy="17" r="17" fill="#2bbf86"/>
        <circle cx="15.5" cy="15.5" r="6.5" fill="none" stroke="#fff" stroke-width="2.5"/>
        <line x1="20.5" y1="20.5" x2="25" y2="25" stroke="#fff" stroke-width="3" stroke-linecap="round"/>
      </svg>
    </div>
    <div class="login">
      <svg width="27" height="27" viewBox="0 0 27 27" aria-hidden="true">
        <circle cx="13.5" cy="13.5" r="12.5" fill="none" stroke="#fff" stroke-width="1.3"/>
        <circle cx="13.5" cy="10.5" r="4.5" fill="none" stroke="#fff" stroke-width="1.3"/>
        <path d="M5.5 22 C7 16.5 20 16.5 21.5 22" fill="none" stroke="#fff" stroke-width="1.3"/>
      </svg>
      <span>LOGIN</span>
    </div>
  </header>

  <article class="card">
    <h1 class="biz-name">Fernwick Home Services</h1>
    <p class="biz-sub">Lawn Care Services - BRAMBLE HEADS, Qld</p>
    <div class="biz-mark" aria-hidden="true"></div>
    <div class="card-rule"></div>

    <div class="media" role="img" aria-label="Map of the service area and company images and videos">
      <span class="media-label">Company Image &amp; Videos</span>
    </div>

    <h2 class="about-title">Nulla convallis, odio a vulputate</h2>
    <p class="about-text">Volutpat, nibh urna finibus arcu, sodales maximus felis quam ac purus. Aenean faucibus risus in ligula convallis sagittis. Nulla facilisi. Sed porta est vel lacus finibus, et pulvinar felis porttitor. Nam aliquet commodo eros, eget mollis metus. Integer pretium nisl urna, ut condimentum lectus mollis a. Phasellus malesuada lacus ut imperdiet scelerisque. Donec pellentesque enim in erat luctus, eget luctus odio posuere. Nunc finibus ipsum blandit elit semper pharetra. Proin porta nisi in enim gravida rhoncus. Vivamus iaculis enim eget cursus consequat. Nam id ex ultricies, rhoncus ante sed, bibendum nulla. Aliquam erat volutpat. Donec dictum auctor consectetur.</p>

    <ul class="services">
      <li>Lawn Care Services</li>
      <li>Lawn Care Services</li>
      <li>Lawn Mowing Services</li>
      <li>Lawn Mowing Services</li>
      <li>Gardening Sevices</li>
      <li>Gardening Sevices</li>
    </ul>

    <h2 class="gallery-title">Photo Gallery</h2>
    <div class="photo photo-house" role="img" aria-label="Photo of a house with a freshly mown front lawn"></div>
    <div class="photo photo-garden" role="img" aria-label="Photo of a landscaped garden bed with stone retaining wall"></div>

    <div class="contact" style="left:27px; top:816px;">
      <svg width="27" height="27" viewBox="0 0 27 27" aria-hidden="true">
        <circle cx="13.5" cy="13.5" r="12.5" fill="none" stroke="#2bbf86" stroke-width="1"/>
        <path d="M9 8 L11.5 7.5 L13 11 L11.5 12.3 C12.3 14 13.5 15.3 15 16 L16.3 14.5 L19.5 16 L19 18.5 C14 19 8.5 13.5 9 8 Z" fill="#2bbf86"/>
      </svg>
      <span>+0099 61 2 5550 1284</span>
    </div>
    <div class="contact" style="left:227px; top:816px;">
      <svg width="29" height="27" viewBox="0 0 29 27" aria-hidden="true">
        <circle cx="14.5" cy="13.5" r="12.5" fill="none" stroke="#2bbf86" stroke-width="1"/>
        <rect x="8" y="9" width="13" height="9" fill="none" stroke="#2bbf86" stroke-width="1.2"/>
        <path d="M8 9 L14.5 14 L21 9" fill="none" stroke="#2bbf86" stroke-width="1.2"/>
      </svg>
      <span>info@fernwickhome.test</span>
    </div>
    <div class="contact" style="left:27px; top:860px;">
      <svg width="27" height="27" viewBox="0 0 27 27" aria-hidden="true">
        <circle cx="13.5" cy="13.5" r="12.5" fill="none" stroke="#2bbf86" stroke-width="1"/>
        <rect x="7.5" y="8" width="12" height="8.5" rx="1" fill="#2bbf86"/>
        <rect x="11.5" y="17" width="4" height="2" fill="#2bbf86"/>
        <rect x="9.5" y="19" width="8" height="1.3" fill="#2bbf86"/>
      </svg>
      <span>www.fernwickhome.test</span>
    </div>
    <div class="contact" style="left:27px; top:902px;">
      <svg width="27" height="27" viewBox="0 0 27 27" aria-hidden="true">
        <circle cx="13.5" cy="13.5" r="12.5" fill="none" stroke="#2bbf86" stroke-width="1"/>
        <path d="M13.5 20.5 C10 16 9 14 9 12 A4.5 4.5 0 0 1 18 12 C18 14 17 16 13.5 20.5 Z" fill="#2bbf86"/>
        <circle cx="13.5" cy="12" r="1.6" fill="#fff"/>
      </svg>
      <span>48 Larchmere Lane, Dunmore, MD 20910</span>
    </div>

    <div class="rating">
      <span class="stars" aria-label="5 stars">
        <svg width="80" height="13" viewBox="0 0 80 13" aria-hidden="true">
          <g fill="#f5c518">
            <path id="star" d="M6.5 0.5 L8.2 4.6 L12.5 4.8 L9.1 7.5 L10.3 11.8 L6.5 9.4 L2.7 11.8 L3.9 7.5 L0.5 4.8 L4.8 4.6 Z"/>
            <use href="#star" x="17"/>
            <use href="#star" x="34"/>
            <use href="#star" x="51"/>
            <use href="#star" x="68"/>
          </g>
        </svg>
      </span>
      <span>22 reviews</span>
    </div>

    <div class="quote-btn">Request Quote</div>
  </article>
</div>
</body>
</html>
```